Events Company- website design

We need a website design for an events company in Brisbane. They have an existing website that needs redesigning....I have attached a design brief with all the details....bear in mind this design will need to be converted onto Dot Net Nuke content management system.

The following elements are required in the Homepage design:

• Logo and phone number across the top - 1300 587 406

• An area for a large flash banner of rotating images on homepage

• Some icons on homepage to include:

• Register interest in a competition

• Check Results

• Download Registration form

• Right Pane – Latest News panel

• Images
need to reflect credibility, professionalism and sports (just use some
example images for now as we’ll need to source some)

Hi everyone

I am meeting with the client next Tuesday to present the designs so will let you know outcome after that.

Cheers
Mavis

Industry/Entity Type

Events

```html
<!DOCTYPE html>
<html lang="en">
<head>
<meta charset="utf-8">
<title>Harcourt Events</title>
<link href="https://fonts.googleapis.com/css2?family=Arimo:wght@400;700&display=swap" rel="stylesheet">
<style>
:root{
  --red:#d0112b;
  --purple:#3b2f72;
  --navy:#2c2a6b;
  --grey-bg:#f6f6f6;
  --panel:#f3f3f3;
  --text:#333;
  --muted:#c2c2c2;
  --dark:#3a3a3a;
}
*{box-sizing:border-box;margin:0;padding:0}
html,body{width:1152px;height:1200px;overflow:hidden}
body{background:#fff;font-family:"Arimo",Arial,sans-serif;color:var(--text);position:relative}
.header{position:absolute;left:0;top:0;width:1152px;height:117px;background:var(--grey-bg)}
.logo{position:absolute;left:117px;top:36px;display:flex;align-items:center;gap:8px}
.logo-mark{width:15px;height:15px;background:var(--red)}
.logo-name{font-size:26px;font-weight:700;color:var(--red);letter-spacing:.3px}
.phone{position:absolute;left:756px;top:24px;font-size:21px;font-weight:700;color:var(--purple);letter-spacing:2px;word-spacing:8px;white-space:nowrap}
.toplinks{position:absolute;left:934px;top:29px;font-size:11px;color:#333;white-space:nowrap}
.search{position:absolute;left:795px;top:61px;display:flex;gap:21px}
.search-input{width:167px;height:25px;border:1px solid #333;background:#fff;font-size:11px;padding:6px 11px;white-space:nowrap}
.search-btn{width:55px;height:25px;background:var(--dark);color:#fff;font-size:11px;text-align:center;line-height:25px}
.nav{position:absolute;left:0;top:117px;width:1152px;height:34px;background:var(--red);border-bottom:3px solid var(--purple)}
.nav ul{list-style:none;display:flex;position:absolute;left:117px;top:0}
.nav li{color:#fff;font-size:13px;line-height:31px;padding:0 11px;height:31px;white-space:nowrap}
.nav li.active{border-bottom:3px solid #fff}
.banner{position:absolute;left:117px;top:181px;width:922px;height:248px;background:linear-gradient(180deg,#8a8f96 0%,#5d6168 50%,#b8bbbf 100%)}
.banner-caption{position:absolute;left:0;bottom:0;width:100%;height:57px;background:rgba(40,40,40,.85);color:#fff;font-size:30px;letter-spacing:1px;padding:12px 20px;white-space:nowrap}
.box{position:absolute;background:var(--panel);padding:18px 17px}
.box h2{font-size:19px;font-weight:400;color:var(--navy);margin-bottom:16px}
.box p{font-size:12.3px;line-height:15px;margin-bottom:15px;color:#333}
.who{left:117px;top:441px;width:641px;height:248px}
.clients{left:117px;top:700px;width:641px;height:370px}
.logo-grid{position:absolute;left:19px;top:129px;width:608px;height:225px;background:#fff}
.client{position:absolute;width:130px;height:58px;display:flex;align-items:center;justify-content:center;gap:6px;font-size:14px;font-weight:700;color:#444;white-space:nowrap}
.client i{width:10px;height:10px;background:#888;display:block}
.viewmore{position:absolute;left:509px;top:165px;font-size:11px;color:var(--red);text-decoration:underline}
.side{position:absolute;left:780px;top:441px;width:260px;height:629px;background:var(--panel)}
.reg-btn{position:absolute;left:29px;top:12px;width:198px;height:35px;background:var(--dark);color:#fff;font-size:15px;text-align:center;line-height:35px;letter-spacing:.3px}
.rule{position:absolute;left:0;width:260px;height:4px;border-top:1px solid #777;border-bottom:1px solid #777}
.rule.red{border-color:var(--red)}
.actions{position:absolute;left:8px;top:93px;list-style:none}
.actions li{display:flex;align-items:center;gap:16px;height:33px;font-size:14.5px;color:#333;white-space:nowrap}
.actions svg{width:22px;height:22px}
.news-head{position:absolute;left:0;top:217px;width:260px;height:34px;background:#666;color:#fff;font-size:14.5px;text-align:center;line-height:34px}
.news{position:absolute;left:15px;top:263px;width:235px}
.news-item{margin-bottom:13px}
.news-title{font-size:13.5px;line-height:16px;color:var(--navy)}
.news-date{font-size:12.5px;color:var(--muted);margin:2px 0 6px}
.news-more{font-size:10.5px;color:var(--red);text-decoration:underline}
.footer{position:absolute;left:0;top:1088px;width:1152px;height:112px;background:var(--grey-bg);border-top:3px double var(--purple)}
.office{position:absolute;left:117px;top:29px;font-size:11px;color:var(--navy)}
.office h3{font-size:11.5px;font-weight:700;margin-bottom:10px}
.office .row{display:flex;gap:26px;margin-bottom:11px}
.office .row span:first-child{width:100px}
.fbtns{position:absolute;left:564px;top:23px;display:flex;gap:32px}
.fbtn{width:142px;height:39px;border:1px solid #ddd;border-radius:20px;background:#fff;display:flex;align-items:center;padding:0 12px;gap:8px;font-size:10.5px;font-weight:700;color:#444;white-space:nowrap}
.fbtn svg{width:18px;height:22px;flex:none}
.fbtn span{flex:1;text-align:right}
.copy{position:absolute;left:879px;top:92px;font-size:11px;color:var(--navy);white-space:nowrap}
</style>
</head>
<body>
<header class="header">
  <div class="logo"><span class="logo-mark"></span><span class="logo-name">Harcourt Events</span></div>
  <div class="phone">1300 587 406</div>
  <div class="toplinks">| &nbsp;Link &nbsp;| &nbsp;Contact Us &nbsp;|</div>
  <div class="search"><div class="search-input">Type in your words ..</div><div class="search-btn">Search</div></div>
</header>
<nav class="nav"><ul>
  <li class="active">Home</li><li>Corporate Profile</li><li>Consultancy Services</li><li>Products</li><li>Sonsorship</li><li>Personal Training</li><li>Helth &amp; Fitness Programs</li><li>Competitions &amp; Events</li>
</ul></nav>
<section class="banner" role="img" aria-label="Close-up photo of marathon runners' legs and shoes on a road">
  <div class="banner-caption">RIVERLINE MARATHONE 2009</div>
</section>
<section class="box who">
  <h2>WHO ARE WE?</h2>
  <p>Harcourt Events is a privately run sporting event organiser and health and fitness programs provider committed to the improvement and betterment of the health and well being of individuals and corporations throughout Australia.</p>
  <p>Our philosophy is simple, we are the “health and well being specialists” that motivate individuals within a corporation so that they can perform better in their work functions with more consistency, drive and balance. In doing so, we have regularly achieved results for individuals and corporations, which have led to, reduced stress and sick leave and a happier and healthy work force.</p>
  <p>Each week, we have over 45 people that run our organised events and sporting and social activities. Our Managing Director, Leon Harcourt leads the charge in developing an impressive range of services, which specifically meet the needs of modern day businesses in the corporate health and sporting event arena.</p>
</section>
<section class="box clients">
  <h2>CLIENTS</h2>
  <p>Leon Harcourt’s current and previous client list is nothing short of impressive! He has worked with numerous individuals and groups that work for some of the Top 100 Australian and International Companies.</p>
  <p>Some of which include:</p>
  <div class="logo-grid">
    <div class="client" style="left:29px;top:34px"><i></i>Kestrel Finance</div>
    <div class="client" style="left:173px;top:34px">Halden Group</div>
    <div class="client" style="left:316px;top:34px">Brightline</div>
    <div class="client" style="left:459px;top:34px">Sonaro</div>
    <div class="client" style="left:29px;top:122px"><i></i>Marlow Bank</div>
    <div class="client" style="left:173px;top:122px">Netharbor</div>
    <div class="client" style="left:316px;top:122px">Quillcom</div>
    <div class="viewmore">view more</div>
  </div>
</section>
<aside class="side">
  <div class="reg-btn">Register Your Team</div>
  <div class="rule" style="top:74px"></div>
  <ul class="actions">
    <li><svg viewBox="0 0 22 22"><path d="M16 2l3 3-10 12-4 1 1-4z" fill="none" stroke="#333" stroke-width="1.5"/><path d="M3 20h16" stroke="#333"/></svg>Register interest in a competition</li>
    <li><svg viewBox="0 0 22 22"><path d="M2 12l6 6L20 4" fill="none" stroke="#333" stroke-width="3"/></svg>Check Results</li>
    <li><svg viewBox="0 0 22 22"><path d="M7 2h8v9h5l-9 10-9-10h5z" fill="#333"/></svg>Download Registration form</li>
  </ul>
  <div class="rule red" style="top:201px"></div>
  <div class="news-head">Latest News</div>
  <div class="news">
    <div class="news-item"><div class="news-title">Bayline pedal ahead with 2010 event</div><div class="news-date">Posted on April 28, 2009</div><span class="news-more">read more</span></div>
    <div class="news-item"><div class="news-title">Singapore Runners Race Along Street Circuit in Sixth Crestmore Corporate Challenge</div><div class="news-date">Posted on April 16, 2009</div><span class="news-more">read more</span></div>
    <div class="news-item"><div class="news-title">New Race Route Makes the Crestmore Corporate Challenge 2009 Even More Thrilling!</div><div class="news-date">Posted on March 17, 2009</div><span class="news-more">read more</span></div>
    <div class="news-item"><div class="news-title">Pro-cycling a Big Hit in Singapore</div><div class="news-date">Posted on February 24, 2009</div><span class="news-more">read more</span></div>
  </div>
</aside>
<footer class="footer">
  <div class="office">
    <h3>NATIONAL HEAD OFFICE</h3>
    <div class="row"><span>Ph: 1300 587 406</span><span>42 Linden Street</span></div>
    <div class="row"><span>Fax: 02 9318 5570</span><span>Westmere NSW 2071</span></div>
  </div>
  <div class="fbtns">
    <div class="fbtn"><svg viewBox="0 0 18 22"><path d="M1 1h11l5 5v15H1z" fill="none" stroke="#d0112b" stroke-width="1.5"/><path d="M5 16l7-7" stroke="#d0112b"/></svg><span>REGISTER</span></div>
    <div class="fbtn"><svg viewBox="0 0 18 22"><path d="M1 1h11l5 5v15H1z" fill="none" stroke="#d0112b" stroke-width="1.5"/><path d="M7 7h4v4h2l-4 5-4-5h2z" fill="#d0112b"/></svg><span>DOWNLOAD</span></div>
    <div class="fbtn"><svg viewBox="0 0 18 22"><path d="M1 1h11l5 5v15H1z" fill="none" stroke="#d0112b" stroke-width="1.5"/><path d="M5 12l3 3 5-6" fill="none" stroke="#d0112b" stroke-width="1.5"/></svg><span>CHECK RESULTS</span></div>
  </div>
  <div class="copy">Copyright 2009. Harcourt Events</div>
</footer>
</body>
</html>
```